Book Cover- KEEPSAKES Coming of Age near Tallow Creek, Nebraska: One Quiet Prairie River Hamlet

Lantern Field Publishing is publishing a book
Book Title: KEEPSAKES Coming of Age near Tallow Creek, Nebraska
Subtitle: One Quiet Prairie River Hamlet
Author: Dana Whitcombe
This is a serious of stories and reflections of the author's experiences growing up in small town called Tallow Creek, Colorado.

Front Cover Brief: We would like to have the first picture uploaded below - picture of mountains with fireworks included in the front cover design
Please include
Author Name: Dana Whitcombe

Back Cover Brief: The second image of the road included in the back cover design.
Please include the text- by: Dana Whitcombe.
Along with this text:

Tallow Creek is miraculous. Being touched by the magic of this beautiful place is my motivation to share the experience.

I was blessed to grow up in a beautiful town and was raised by a loving family during an amazing time of global change. Shared experiences are an exceptional way for us all to learn, grow, and be entertained. I hope you enjoy the stories as much as I enjoyed writing them. After all, the name of Tallow Creek could well be “Magic.”

This book is a collection of memories and shared experiences from growing up with friends and family in One Quiet Prairie River Hamlet. These recollections were written from a place in my heart where love lives. I loved growing up in Tallow Creek.

KEEPSAKES Coming Of Age Near Tallow Creek, Nebraska, is my effort to encourage others to reflect and share their experiences of growing up, wherever that may have been.

If space allows include the name of the publishing company: Lantern Field Publishing on back cover

Spine - We also need a spine with the title of the book Coming of Age near Tallow Creek, Nebraska : One Quiet PRAIRIE River Hamlet and Author's name - Dana Whitcombe.

```html
<!DOCTYPE html>
<html lang="en">
<head>
<meta charset="utf-8">
<title>KEEPSAKES – Book Cover Wrap</title>
<link rel="stylesheet" href="https://fonts.googleapis.com/css2?family=Baskervville&family=Libre+Baskerville&display=swap">
<style>
  :root {
    --sky-top: #2b8be0;
    --sky-mid: #6fb6ee;
    --sky-low: #c9e4f8;
    --spine: #3d3966;
    --title-ink: #3d3966;
    --body-ink: #262a38;
    --white: #ffffff;
  }
  html, body {
    margin: 0;
    padding: 0;
    width: 1200px;
    height: 874px;
    overflow: hidden;
    background: #ffffff;
  }
  .cover-wrap {
    position: relative;
    width: 1200px;
    height: 874px;
    overflow: hidden;
    font-family: "Baskervville", "Libre Baskerville", serif;
  }

  /* Back cover */
  .back-cover {
    position: absolute;
    left: 0; top: 0;
    width: 578px; height: 874px;
    background: linear-gradient(180deg, var(--sky-top) 0%, var(--sky-mid) 45%, var(--sky-low) 80%, #e4eef4 100%);
  }
  .back-blurb {
    position: absolute;
    left: 30px; top: 216px;
    width: 518px;
    text-align: center;
    color: var(--body-ink);
    font-size: 17.2px;
    line-height: 20px;
  }
  .back-blurb p { margin: 0 0 20px; }
  .road-photo {
    position: absolute;
    left: 0; top: 690px;
    width: 578px; height: 184px;
    background: linear-gradient(180deg, rgba(201,228,248,0) 0%, #9fb0b8 22%, #6f7f78 45%, #8a9570 62%, #5e6266 80%, #44484d 100%);
  }
  .barcode-area {
    position: absolute;
    left: 365px; top: 726px;
    width: 188px; height: 111px;
    background: var(--white);
  }

  /* Spine */
  .spine {
    position: absolute;
    left: 578px; top: 0;
    width: 42px; height: 874px;
    background: var(--spine);
    color: var(--white);
  }
  .spine-text {
    position: absolute;
    left: 0; top: 36px;
    width: 42px;
    height: 620px;
    overflow: hidden;
    writing-mode: vertical-rl;
    line-height: 42px;
    white-space: nowrap;
  }
  .spine-title { font-size: 13px; letter-spacing: 0.2px; }
  .spine-subtitle { font-size: 13.5px; margin-top: 12px; display: inline-block; }
  .spine-author {
    position: absolute;
    left: 0; top: 684px;
    width: 42px;
    writing-mode: vertical-rl;
    line-height: 42px;
    font-size: 19px;
    white-space: nowrap;
  }

  /* Front cover */
  .front-cover {
    position: absolute;
    left: 620px; top: 0;
    width: 580px; height: 874px;
    background: linear-gradient(180deg, #4f9fe6 0%, #86c1ef 30%, #b6d8f2 45%, #c9e0f2 100%);
  }
  .front-photo {
    position: absolute;
    left: 0; top: 345px;
    width: 580px; height: 529px;
    background: linear-gradient(180deg, rgba(185,210,238,0) 0%, #8b93bd 14%, #5d6797 32%, #6c7556 52%, #34522f 70%, #1f3b23 100%);
  }
  .front-title {
    position: absolute;
    left: 0; top: 92px;
    width: 580px;
    margin: 0;
    text-align: center;
    color: var(--title-ink);
    font-weight: 400;
    font-size: 60px;
    line-height: 64px;
  }
  .front-subtitle {
    position: absolute;
    left: 0; top: 161px;
    width: 580px;
    margin: 0;
    text-align: center;
    color: var(--title-ink);
    font-weight: 400;
    font-size: 17.5px;
    letter-spacing: 1px;
  }
  .front-tagline {
    position: absolute;
    left: 0; top: 266px;
    width: 580px;
    margin: 0;
    text-align: center;
    color: var(--body-ink);
    font-size: 23px;
  }
  .front-author {
    position: absolute;
    left: 150px; top: 803px;
    width: 440px;
    text-align: center;
    color: var(--white);
    font-size: 30px;
  }
</style>
</head>
<body>
<div class="cover-wrap">

  <section class="back-cover">
    <div class="back-blurb">
      <p>Tallow Creek is miraculous. Being touched by the magic of this beautiful place is my motivation to share the experience.</p>
      <p>I was blessed to grow up in a beautiful town and was raised by a loving family during an amazing time of global change. Shared experiences are an exceptional way for us all to learn, grow, and be entertained. I hope you enjoy the stories as much as I enjoyed writing them. After all, the name of Tallow Creek could well be “Magic.”</p>
      <p>This book is a collection of memories and shared experiences from growing up with friends and family in One Quiet Prairie River Hamlet. These recollections were written from a place in my heart where love lives. I loved growing up in Tallow Creek.</p>
      <p>KEEPSAKES Coming Of Age Near Tallow Creek, Nebraska, is my effort to encourage others to reflect and share their experiences of growing up, wherever that may have been.</p>
    </div>
    <div class="road-photo" role="img" aria-label="Photograph of a straight country road leading toward misty mountains under a blue sky"></div>
    <div class="barcode-area"></div>
  </section>

  <section class="spine">
    <div class="spine-text">
      <span class="spine-title">COMING OF AGE NEAR TALLOW CREEK, NEBRASKA</span><span class="spine-subtitle">One Quiet Prairie River Hamlet</span>
    </div>
    <div class="spine-author">Dana Whitcombe</div>
  </section>

  <section class="front-cover">
    <div class="front-photo" role="img" aria-label="Photograph of a mountain valley town at dusk with snowy peaks and fireworks bursting over the ridge"></div>
    <h1 class="front-title">KEEPSAKES</h1>
    <h2 class="front-subtitle">COMING OF AGE NEAR TALLOW CREEK, NEBRASKA</h2>
    <p class="front-tagline">One Quiet Prairie River Hamlet</p>
    <div class="front-author">Dana Whitcombe</div>
  </section>

</div>
</body>
</html>
```